Therapy Department Recruitment Flyer

Recruitment flyer similar to nursing one attached but for Occupational Therapy and Physical Therapy. Please use pictures depicting therapy services being provided to elderly population.

```html
<!DOCTYPE html>
<html lang="en">
<head>
<meta charset="utf-8">
<title>Therapy Positions Flyer</title>
<link href="https://fonts.googleapis.com/css2?family=Oswald:wght@500&family=Source+Sans+3:wght@400;600;700&display=swap" rel="stylesheet">
<style>
  :root{
    --slate:#3d434f;
    --slate-mid:#9aa0ae;
    --slate-light:#c9ccd3;
    --ink:#3a3d44;
    --body:#55585f;
    --paper:#ffffff;
    --backdrop:#e9e9eb;
    --photo-a:#e4e8ec;
    --photo-b:#a9b6c2;
    --photo-c:#6e8fa8;
  }
  *{box-sizing:border-box;margin:0;padding:0}
  html,body{width:1200px;height:800px;overflow:hidden;background:var(--backdrop)}
  body{position:relative;font-family:"Source Sans 3",Arial,sans-serif}
  .flyer{
    position:absolute;left:332px;top:20px;width:595px;height:844px;
    transform:scale(.9);transform-origin:0 0;background:var(--paper);
    overflow:hidden;box-shadow:0 4px 18px rgba(0,0,0,.18);
  }
  .flyer-art{position:absolute;inset:0}
  .title{
    position:absolute;left:18px;top:26px;font-family:"Oswald",Impact,sans-serif;
    font-weight:500;font-size:33px;color:#fff;letter-spacing:.2px;line-height:1;
  }
  .brand{
    position:absolute;left:420px;top:52px;font-weight:600;font-size:23px;
    line-height:1.1;color:var(--slate);display:flex;align-items:center;gap:8px;
  }
  .brand-mark{width:12px;height:12px;border-radius:50%;background:var(--slate)}
  .headline{
    position:absolute;left:31px;top:470px;width:520px;font-weight:700;font-size:17.5px;
    line-height:23px;color:var(--ink);text-transform:uppercase;
  }
  .intro{
    position:absolute;left:35px;top:528px;width:532px;font-size:13.4px;line-height:22px;
    color:var(--body);text-align:justify;
  }
  .forest{position:absolute;left:0;top:712px;width:595px;height:96px}
  .info-box{
    position:absolute;top:608px;width:260px;height:106px;border:1px solid var(--slate-mid);
    border-radius:6px;background:#fff;overflow:hidden;z-index:2;
  }
  .info-box.positions{left:31px}
  .info-box.contact{left:306px}
  .info-box h3{
    background:var(--slate-mid);color:#fff;font-weight:600;font-size:14px;
    height:31px;line-height:31px;padding-left:12px;
  }
  .info-box ul{list-style:none;padding:8px 0 0 16px}
  .info-box li{font-size:13.4px;color:var(--ink);line-height:22px;display:flex;align-items:center;gap:8px}
  .bullet{width:10px;height:10px}
  .contact-name{font-size:12.8px;color:var(--ink);padding:3px 0 0 20px;line-height:20px;white-space:nowrap}
  .contact-line{font-size:11.5px;color:var(--ink);padding-left:18px;line-height:22px;display:flex;align-items:center;gap:9px;white-space:nowrap}
  .contact-line svg{width:11px;height:11px}
  .footer-bar{position:absolute;left:0;top:806px;width:595px;height:38px;background:var(--slate)}
  .phone-tab{
    position:absolute;left:0;top:786px;width:272px;height:58px;background:var(--slate-mid);
    clip-path:polygon(0 0,250px 0,272px 58px,0 58px);display:flex;align-items:center;
    padding-left:30px;gap:8px;color:#fff;font-family:"Oswald",Impact,sans-serif;font-weight:500;font-size:26px;
  }
  .phone-tab svg{width:22px;height:32px}
  .address{
    position:absolute;right:32px;top:815px;color:#e4e6ea;font-size:12.5px;letter-spacing:.6px;
    display:flex;align-items:center;gap:10px;
  }
  .address svg{width:10px;height:13px}
</style>
</head>
<body>
<main class="flyer">
  <svg class="flyer-art" viewBox="0 0 595 844" width="595" height="844" aria-hidden="false">
    <defs>
      <linearGradient id="photoTone" x1="0" y1="0" x2="1" y2="1">
        <stop offset="0" stop-color="var(--photo-a)"/>
        <stop offset=".55" stop-color="var(--photo-b)"/>
        <stop offset="1" stop-color="var(--photo-c)"/>
      </linearGradient>
    </defs>
    <rect role="img" aria-label="Photo: a therapist guiding an elderly woman through a balance exercise in a bright therapy gym" x="0" y="90" width="595" height="360" fill="url(#photoTone)"/>
    <path d="M0 0H595V22C500 14 390 38 300 82C230 114 120 112 0 104Z" fill="var(--slate)"/>
    <path d="M300 82C390 38 500 14 595 22V122C520 146 400 142 300 82Z" fill="var(--paper)"/>
    <path d="M0 108C120 116 230 118 300 86C390 42 500 18 595 26" fill="none" stroke="var(--slate-mid)" stroke-width="3"/>
    <path d="M0 412C110 368 240 372 350 402C450 430 530 426 595 404V844H0Z" fill="var(--slate)"/>
    <path d="M0 432C110 392 240 396 350 424C450 448 530 444 595 428V844H0Z" fill="var(--paper)"/>
  </svg>

  <h1 class="title">THEREAPY POSITIONS</h1>
  <div class="brand"><span class="brand-mark"></span><span>Silver Aspen<br>Care Center</span></div>

  <h2 class="headline">We are seeking caring and compassionate<br>therapist to join our team</h2>
  <p class="intro">Silver Aspen Care Centar is Skilled Nursing Facility in Cedar Ridge, Nevada.At the hart of Silver Aspen Country, Cedar Ridge is frendly, rural mountain town in Estern Nevada that is rich with art and history, as well as an abundance of oppotunities for outdoor adventure.</p>

  <svg class="forest" viewBox="0 0 595 96" role="img" aria-label="Soft grey forest treeline decoration">
    <defs>
      <linearGradient id="forestTone" x1="0" y1="0" x2="0" y2="1">
        <stop offset="0" stop-color="#ffffff"/>
        <stop offset=".45" stop-color="var(--slate-light)"/>
        <stop offset="1" stop-color="#b3b7bf"/>
      </linearGradient>
    </defs>
    <rect width="595" height="96" fill="url(#forestTone)"/>
  </svg>

  <section class="info-box positions">
    <h3>Thereapy Positions</h3>
    <ul>
      <li><svg class="bullet" viewBox="0 0 10 10"><circle cx="5" cy="5" r="5" fill="var(--slate)"/><path d="M4 3l2 2-2 2" stroke="#fff" stroke-width="1.3" fill="none"/></svg>Physical Therapist</li>
      <li><svg class="bullet" viewBox="0 0 10 10"><circle cx="5" cy="5" r="5" fill="var(--slate)"/><path d="M4 3l2 2-2 2" stroke="#fff" stroke-width="1.3" fill="none"/></svg>Occupational Therapist</li>
    </ul>
  </section>

  <section class="info-box contact">
    <h3>Recruiting Contact</h3>
    <p class="contact-name">Dana Merrow - Director of Nursing Services</p>
    <p class="contact-line"><svg viewBox="0 0 12 12"><path d="M2.5 1l2 2.3-1.2 1.4c.8 1.6 1.9 2.7 3.5 3.5L8.2 7l2.3 2-1.2 2C5 10.6 1.4 7 1 2.7Z" fill="var(--slate)"/></svg>555 014 2290 ext 2204</p>
    <p class="contact-line"><svg viewBox="0 0 12 12"><rect x="0.5" y="2" width="11" height="8" fill="var(--slate)"/><path d="M1 2.5l5 4 5-4" stroke="#fff" stroke-width="1" fill="none"/></svg>dmerrow@silveraspencare.com</p>
  </section>

  <div class="footer-bar"></div>
  <div class="phone-tab">
    <svg viewBox="0 0 22 32"><rect x="2" y="1" width="18" height="30" rx="3" fill="none" stroke="#fff" stroke-width="2.4"/><rect x="4.5" y="25" width="13" height="2" fill="#fff"/></svg>
    <span>+1 555-014-2290</span>
  </div>
  <p class="address">2400 Juniper Way, Cedar Ridge, NV 89000
    <svg viewBox="0 0 10 13"><path d="M5 0a4 4 0 0 1 4 4c0 3-4 9-4 9S1 7 1 4a4 4 0 0 1 4-4Z" fill="#e4e6ea"/><circle cx="5" cy="4" r="1.5" fill="var(--slate)"/></svg>
  </p>
</main>
</body>
</html>
```